Brightmoor Specialty floor services

Create a one page flyer 8.5x11 with picture and text overlay as follows:
Brightmoor Specialty Floor Services
Expert Epoxy & Terrazzo Flooring – Installation & Repair
As a trusted janitorial and maintenance company, Brightmoor is proud to offer professional flooring services to restore and enhance your facility’s appearance.
Our Floor Services Include:
Epoxy Flooring – Durable, seamless, and chemical-resistant surfaces perfect for industrial, commercial, and retail environments.
• New Epoxy Floor Installation
• Epoxy Floor Repairs & Resurfacing
Terrazzo Flooring – Elegant and long-lasting flooring for high-traffic spaces with stunning, polished finishes.
• New Terrazzo Floor Installation
• Terrazzo Repairs, Restoration & Polishing
Why Choose Brightmoor?
Professional Craftsmanship – High-quality materials and precision installation
Minimal Downtime – We work around your schedule
Seamless Integration – Combine with our janitorial and facility maintenance services
Serving a Range of Industries – Offices, Retail, Healthcare, Education & More
Contact Us Today to Refresh Your Floors!
905-555-0147
support@brightmoor-example.ca
Toll-Free: 1-877-555-014

add this text as well: Our Specialized Services Include:
✅ Epoxy Coating
Durable, chemical-resistant surfaces for seamless, easy-to-maintain floors.

✅ Polyaspartic Coating
Fast-curing, UV-stable finish — ideal for high-traffic areas and quick turnarounds.

✅ Polyurethane Coating
Flexible and long-lasting; excellent abrasion resistance and gloss retention.

✅ Polished Concrete
A high-end, reflective finish with low maintenance — perfect for modern industrial spaces.

✅ Self-Leveling Systems
Smooth, even finishes that restore damaged or uneven concrete floors.

✅ Urethane Cement
Heavy-duty flooring ideal for harsh environments with thermal shock or chemical exposure.

✅ Moisture Prevention & Waterproofing Membrane
Protect your floors from moisture vapor damage and extend their lifespan.

```html
<!DOCTYPE html>
<html lang="en">
<head>
<meta charset="utf-8">
<title>Brightmoor Specialty Floor Services</title>
<link rel="stylesheet" href="https://fonts.googleapis.com/css2?family=Anton&family=Outfit:wght@300;400;500;600&display=swap">
<style>
  :root {
    --brand-blue: #037bbd;
    --bright-blue: #0a78d1;
    --cyan: #1ee3ef;
    --charcoal: #333333;
    --ink: #2a2a2a;
    --body-grey: #3d3d3d;
    --panel-grey: #f3f3f3;
    --page-bg: #e9eef4;
    --white: #ffffff;
  }
  * { box-sizing: border-box; margin: 0; padding: 0; }
  html, body { width: 993px; height: 1200px; overflow: hidden; background: var(--page-bg); }
  body { font-family: "Outfit", sans-serif; color: var(--body-grey); }

  .flyer {
    position: absolute; left: 33px; top: 0; width: 927px; height: 1200px;
    background: linear-gradient(180deg, #ffffff 40%, #cfe5f2 100%);
    overflow: hidden;
  }
  .abs { position: absolute; }
  .nowrap { white-space: nowrap; }

  .hero-panel {
    left: 33px; top: 0; width: 455px; height: 438px;
    background: var(--brand-blue); border-bottom-left-radius: 20px;
  }
  .hero-title {
    left: 58px; top: 42px; font-family: "Anton", sans-serif; color: var(--white);
    font-size: 74px; line-height: 96px; letter-spacing: -1.5px;
  }
  .hero-subtitle {
    left: 58px; top: 139px; color: var(--cyan); font-weight: 600;
    font-size: 51px; line-height: 53px; letter-spacing: -1.2px;
  }
  .hero-intro {
    left: 60px; top: 251px; color: var(--white);
    font-size: 19.5px; line-height: 24.3px; font-weight: 300; white-space: nowrap;
  }
  .hero-intro strong { font-weight: 400; }

  .brand-name {
    left: 513px; top: 48px; color: var(--brand-blue); font-size: 40px;
    font-weight: 400; letter-spacing: 6px; display: flex; align-items: center; gap: 14px;
  }
  .brand-name .mark { width: 14px; height: 14px; background: var(--brand-blue); }

  .why-panel {
    left: 424px; top: 136px; width: 470px; height: 409px;
    background: var(--charcoal); border-radius: 20px;
  }
  .why-title {
    left: 454px; top: 166px; font-family: "Anton", sans-serif; font-size: 42px;
    line-height: 46px; color: var(--white);
  }
  .why-title span { color: var(--cyan); display: block; }
  .why-list { left: 445px; top: 277px; list-style: none; }
  .why-list li {
    position: relative; padding-left: 36px; color: var(--white); white-space: nowrap;
    font-size: 19.5px; line-height: 24.3px; font-weight: 300; margin-bottom: 13.5px;
  }
  .why-list li strong { font-weight: 400; }
  .why-list svg { position: absolute; left: 0; top: 6px; }

  .deco { border-radius: 10px; }
  .deco-frames-top { left: 738px; top: 139px; width: 160px; height: 124px;
    background: linear-gradient(135deg, #58d3f2, #1f5fe0); opacity: .85; }
  .deco-star { left: 372px; top: 690px; width: 84px; height: 100px;
    background: radial-gradient(circle, #2a7fe6 40%, #1550c8 100%); border-radius: 40%; }
  .deco-frames-bottom { left: 316px; top: 1045px; width: 142px; height: 134px;
    background: linear-gradient(135deg, #1f5fe0, #58d3f2); opacity: .8; }

  .section-title { font-family: "Anton", sans-serif; color: var(--ink); font-size: 40px; line-height: 48px; }
  .section-copy { font-size: 19.5px; line-height: 24.3px; font-weight: 300; white-space: nowrap; }
  .chevron-list { list-style: none; }
  .chevron-list li {
    position: relative; padding-left: 26px; font-size: 19.5px; line-height: 24.3px;
    font-weight: 300; margin-bottom: 4.5px; white-space: nowrap;
  }
  .chevron-list svg { position: absolute; left: 2px; top: 7px; }

  .epoxy-title { left: 60px; top: 460px; }
  .epoxy-copy { left: 60px; top: 512px; }
  .epoxy-list { left: 60px; top: 623px; }
  .terrazzo-title { left: 60px; top: 706px; }
  .terrazzo-copy { left: 60px; top: 757px; }
  .terrazzo-list { left: 60px; top: 839px; }

  .cta-lead { left: 60px; top: 935px; font-family: "Anton", sans-serif; font-size: 31px; line-height: 36px; color: var(--ink); }
  .cta-main {
    left: 55px; top: 975px; font-family: "Anton", sans-serif; font-size: 39px;
    color: var(--bright-blue); transform: rotate(-2deg); transform-origin: left bottom;
    background: var(--white); padding: 0 5px; line-height: 46px; white-space: nowrap;
    box-shadow: 0 4px 8px rgba(0,0,0,.12);
  }
  .contact-box {
    left: 54px; top: 1022px; width: 300px; height: 128px; background: var(--brand-blue);
    border-radius: 0 0 10px 10px; padding: 18px 0 0 20px;
  }
  .contact-line {
    display: flex; align-items: center; gap: 10px; color: var(--white);
    font-weight: 600; font-size: 15.5px; height: 30px; white-space: nowrap; letter-spacing: -0.1px;
  }
  .contact-line svg { flex: none; }
  .contact-line.primary { font-size: 24px; height: 34px; letter-spacing: 0; }

  .services-panel { left: 443px; top: 545px; width: 433px; height: 655px; background: var(--panel-grey); }
  .services-title { left: 474px; top: 577px; font-family: "Anton", sans-serif; font-size: 33px; line-height: 46px; color: var(--ink); }
  .services-title span { color: var(--bright-blue); }
  .service { left: 474px; white-space: nowrap; }
  .service h3 { font-weight: 400; font-size: 17.5px; line-height: 21.5px; color: var(--ink); }
  .service p { font-weight: 300; font-size: 17px; line-height: 21.5px; color: var(--body-grey); letter-spacing: -0.1px; }
</style>
</head>
<body>
<main class="flyer">
  <div class="abs hero-panel"></div>
  <h1 class="abs hero-title">BRIGHTMOOR</h1>
  <h2 class="abs hero-subtitle">Specialty Floor<br>Services</h2>
  <p class="abs hero-intro"><strong>Expert Epoxy &amp; Terrazzo Flooring –</strong><br>Installation &amp; Repair. As a trusted<br>janitorial and maintenance company,<br>We are proud to offer professional<br>flooring services to restore &amp; enhance<br>your facility’s appearance</p>

  <div class="abs brand-name"><span>BRIGHTMOOR</span><span class="mark"></span></div>

  <div class="abs why-panel"></div>
  <h2 class="abs why-title">WHY CHOOSE <span>BRIGHTMOOR?</span></h2>
  <div class="abs deco deco-frames-top" role="img" aria-label="Decorative 3D blue interlocking square frames"></div>
  <ul class="abs why-list">
    <li><svg width="16" height="12" viewBox="0 0 16 12"><path d="M1 6l5 5 9-10" fill="none" stroke="#1ee3ef" stroke-width="2"/></svg><strong>Professional Craftsmanship</strong> High quality<br>materials and precision installation</li>
    <li><svg width="16" height="12" viewBox="0 0 16 12"><path d="M1 6l5 5 9-10" fill="none" stroke="#1ee3ef" stroke-width="2"/></svg><strong>Minimal Downtime</strong> We work around your<br>schedule</li>
    <li><svg width="16" height="12" viewBox="0 0 16 12"><path d="M1 6l5 5 9-10" fill="none" stroke="#1ee3ef" stroke-width="2"/></svg><strong>Seamless Integration</strong> Combine with our<br>janitorial &amp; facility maintenance services</li>
    <li><svg width="16" height="12" viewBox="0 0 16 12"><path d="M1 6l5 5 9-10" fill="none" stroke="#1ee3ef" stroke-width="2"/></svg><strong>Serving a Range of Industries</strong> Offices,<br>Retail, Healthcare, Education &amp; More</li>
  </ul>

  <h2 class="abs section-title epoxy-title">EPOXY FLOORING</h2>
  <p class="abs section-copy epoxy-copy">Durable, seamless, and chemical<br>resistant surfaces perfect for<br>industrial, commercial, and retail<br>environments.</p>
  <ul class="abs chevron-list epoxy-list">
    <li><svg width="8" height="12" viewBox="0 0 8 12"><path d="M1 1l5 5-5 5" fill="none" stroke="#2a2a2a" stroke-width="1.6"/></svg>New Epoxy Floor Installation</li>
    <li><svg width="8" height="12" viewBox="0 0 8 12"><path d="M1 1l5 5-5 5" fill="none" stroke="#2a2a2a" stroke-width="1.6"/></svg>Epoxy Floor Repairs &amp; Resurfacing</li>
  </ul>

  <h2 class="abs section-title terrazzo-title">TERRAZZO FLOORING</h2>
  <div class="abs deco deco-star" role="img" aria-label="Blue starburst accent"></div>
  <p class="abs section-copy terrazzo-copy">Elegant and long-lasting flooring<br>for high-traffic spaces with stunning,<br>polished finishes.</p>
  <ul class="abs chevron-list terrazzo-list">
    <li><svg width="8" height="12" viewBox="0 0 8 12"><path d="M1 1l5 5-5 5" fill="none" stroke="#2a2a2a" stroke-width="1.6"/></svg>New Terrazzo Floor Installation</li>
    <li><svg width="8" height="12" viewBox="0 0 8 12"><path d="M1 1l5 5-5 5" fill="none" stroke="#2a2a2a" stroke-width="1.6"/></svg>Terrazzo Repairs, Restoration &amp;<br>Polishing</li>
  </ul>

  <p class="abs cta-lead">CONTACT US TODAY TO</p>
  <div class="abs deco deco-frames-bottom" role="img" aria-label="Decorative 3D blue interlocking square frames"></div>
  <div class="abs contact-box">
    <div class="contact-line primary"><svg width="18" height="18" viewBox="0 0 24 24"><path d="M6.6 10.8a15 15 0 006.6 6.6l2.2-2.2a1 1 0 011-.25 11.4 11.4 0 003.6.6 1 1 0 011 1V20a1 1 0 01-1 1A17 17 0 013 4a1 1 0 011-1h3.5a1 1 0 011 1 11.4 11.4 0 00.6 3.6 1 1 0 01-.25 1z" fill="#1ee3ef"/></svg>905-555-0147</div>
    <div class="contact-line"><svg width="18" height="14" viewBox="0 0 24 18"><rect width="24" height="18" rx="2" fill="#1ee3ef"/><path d="M2 3l10 7 10-7" fill="none" stroke="#037bbd" stroke-width="2"/></svg>support@brightmoor-example.ca</div>
    <div class="contact-line"><svg width="18" height="18" viewBox="0 0 24 24"><path d="M6.6 10.8a15 15 0 006.6 6.6l2.2-2.2a1 1 0 011-.25 11.4 11.4 0 003.6.6 1 1 0 011 1V20a1 1 0 01-1 1A17 17 0 013 4a1 1 0 011-1h3.5a1 1 0 011 1 11.4 11.4 0 00.6 3.6 1 1 0 01-.25 1z" fill="#1ee3ef"/></svg>1-877-555-014</div>
  </div>
  <p class="abs cta-main">REFRESH YOUR FLOORS!</p>

  <div class="abs services-panel"></div>
  <h2 class="abs services-title">OUR <span>SPECIALIZED</span> SERVICES</h2>
  <div class="abs service" style="top:625px"><h3>Epoxy Coating</h3><p>Durable, chemical-resistant surfaces for<br>seamless, easy-to-maintain floors.</p></div>
  <div class="abs service" style="top:701px"><h3>Polyaspartic Coating</h3><p>Fast-curing, UV-stable finish — ideal for<br>high-traffic areas and quick turnarounds.</p></div>
  <div class="abs service" style="top:777px"><h3>Polyurethane Coating</h3><p>Flexible and long-lasting; excellent abrasion<br>resistance and gloss retention.</p></div>
  <div class="abs service" style="top:853px"><h3>A Polished Concrete</h3><p>A high end, reflective finish with low maintenance,<br>perfect for modern industrial spaces.</p></div>
  <div class="abs service" style="top:929px"><h3>Self-Leveling Systems</h3><p>Smooth, even finishes that restore damaged or<br>uneven concrete floors.</p></div>
  <div class="abs service" style="top:1005px"><h3>Urethane Cement</h3><p>Heavy duty flooring ideal for harsh environments<br>with thermal shock or chemical exposure.</p></div>
  <div class="abs service" style="top:1081px"><h3>Moisture Prevention &amp; Waterproofing Membrane</h3><p>Protect your floors from moisture vapor damage<br>and extend their lifespan.</p></div>
</main>
</body>
</html>
```